Business Card Design

We are a new residential construction company.our team is made up of young highly skilled tradesman of the next generation of carpenters coming through with new skills and ideas.we chose the name meridian as it means strikingly different from the rest as this is what we plan to be and we would like to portray this in our business card.we like Bold lettering as we want to make a statement, also the use of colour would be great as we want to stand out from the usual plain construction cards and logos.
I have attached a logo sketch I did as a rough idea if you can tidy it up or improve on it would be good.
I have also attached the LBP logo please include this on the card small but still legible.
open to any colourschemes ideas.
thanks
(note)please delete the LBP#804317 off from the card details please.
Industry/Entity Type
Construction
Contact Information for Business Card
MERIDIAN CONSTRUCTION LIMITED
Director:Tom Halvick
Mobile :0217364820
Email:Meridian.Construction@quillpost.example
Address:48 Wendle place,Ashgrove park 2091,Auckland
LBP#BP804317

```html
<!DOCTYPE html>
<html lang="en">
<head>
<meta charset="utf-8">
<title>Meridian Construction Limited — Business Card</title>
<link rel="stylesheet" href="https://fonts.googleapis.com/css2?family=Montserrat:wght@800&family=Questrial&family=Arimo&display=swap">
<style>
  :root {
    --frame: #4a4a4c;
    --ink: #464648;
    --white: #ffffff;
    --card-light: #ffffff;
    --card-mid: #d6d6d7;
    --card-dark: #8e8e90;
    --yellow: #fec92c;
    --pale-grey: #d4d4d6;
    --sky: #8fd7f5;
    --blue: #00aeef;
    --green: #00a651;
    --badge-dark: #111111;
  }
  html, body {
    margin: 0;
    padding: 0;
    overflow: hidden;
  }
  body {
    position: relative;
    width: 1200px;
    height: 725px;
    background: var(--frame);
  }
  .card {
    position: absolute;
    left: 32px;
    top: 30px;
    width: 1136px;
    height: 665px;
    overflow: hidden;
    background: linear-gradient(200deg, var(--card-light) 8%, var(--card-mid) 45%, var(--card-dark) 100%);
  }
  .card-graphics {
    position: absolute;
    left: -32px;
    top: -30px;
    width: 1200px;
    height: 725px;
  }
  .house-illustration {
    position: absolute;
    left: 910px;
    top: 308px;
    width: 223px;
    height: 357px;
    background: linear-gradient(180deg, var(--sky) 0%, var(--blue) 35%, var(--pale-grey) 100%);
    opacity: 0.85;
  }
  .brand {
    position: absolute;
    left: 24px;
    top: 170px;
    display: flex;
    align-items: center;
    gap: 22px;
  }
  .brand-square {
    width: 92px;
    height: 92px;
    background: var(--green);
  }
  .brand-name {
    font-family: "Montserrat", sans-serif;
    font-weight: 800;
    font-size: 138px;
    line-height: 1;
    letter-spacing: 1px;
    color: var(--ink);
    text-transform: uppercase;
  }
  .brand-tagline {
    position: absolute;
    left: 154px;
    top: 278px;
    font-family: "Questrial", sans-serif;
    font-size: 80px;
    line-height: 1;
    color: var(--ink);
    white-space: nowrap;
  }
  .contact {
    position: absolute;
    left: 19px;
    top: 432px;
    font-family: "Arimo", sans-serif;
    color: var(--white);
    white-space: nowrap;
  }
  .contact-director {
    font-size: 42px;
    line-height: 48px;
    margin: 0 0 4px;
  }
  .contact-line {
    font-size: 33px;
    line-height: 37px;
    margin: 0 0 0 3px;
  }
</style>
</head>
<body>
  <main class="card">
    <svg class="card-graphics" viewBox="0 0 1134 685" aria-hidden="true">
      <rect class="accent-bar" x="34" y="366" width="288" height="41" fill="var(--yellow)"/>
      <rect class="accent-bar" x="332" y="366" width="289" height="41" fill="var(--pale-grey)"/>
      <g class="licence-badge">
        <circle cx="1010" cy="100" r="78" fill="var(--white)"/>
        <circle cx="1010" cy="100" r="50" fill="var(--badge-dark)"/>
      </g>
    </svg>

    <div class="house-illustration" role="img" aria-label="Illustration of a house outline with colourful building bars rising behind it"></div>

    <div class="brand">
      <div class="brand-square"></div>
      <div class="brand-name">Meridian</div>
    </div>
    <div class="brand-tagline">Construction Limited</div>

    <section class="contact">
      <p class="contact-director">Director:Tom Halvick</p>
      <p class="contact-line">Mobile :0217364820</p>
      <p class="contact-line">Email:Meridian.Construction@quillpost.example</p>
      <p class="contact-line">Address:48 Wendle place,Ashgrove park 2091,Auckland</p>
    </section>
  </main>
</body>
</html>
```